FurPerks - Dog Coupon Site Design Brief

Project Overview
**Site Name:** TailTrove.com
**Purpose:** A modern coupon aggregation platform specifically for dog and pet-related products and services
**Target Audience:** Dog owners, pet enthusiasts, budget-conscious pet parents

Brand Identity & Visual Direction

Typography
- **Headers:** Modern sans-serif (Inter or similar) - Clean and friendly
- **Body:** Readable sans-serif with good mobile legibility
- **Accent:** Playful but professional font for coupon codes

Design Principles
- **Flat Design:** Clean, minimal with subtle shadows
- **Friendly & Approachable:** Rounded corners, soft edges
- **Trust-Building:** Clear pricing, transparent savings
- **Scannable:** Easy-to-read coupon codes and offers

## User Experience & Functionality

### Homepage Features
1. **Hero Section**
- Clear value proposition
- Search functionality
- Featured savings highlight

2. **Coupon Cards**
- One-click copy functionality
- Clear discount display
- Store/brand logos
- Expiration dates
- "Get Deal" call-to-action

3. **Navigation**
- Categories (Food, Toys, Health, Services, etc.)
- Popular stores
- Latest deals

### Interactive Elements
- **Copy Button:** Instant feedback when coupon copied
- **Deal Pages:** Detailed offer information, terms, store details
- **Search & Filter:** By category, store, discount amount
- **Mobile Menu:** Hamburger navigation for mobile

## Technical Requirements

### Responsive Design
- **Mobile-First:** Optimized for touch interactions
- **Tablet:** Adapted layout for medium screens
- **Desktop:** Full-width utilization with sidebar potential

### Performance
- **Fast Loading:** Optimized images, minimal JavaScript
- **Accessibility:** WCAG compliant, screen reader friendly
- **SEO Optimized:** Structured data for deals and offers

## Content Strategy

### Deal Categories
- Dog Food & Treats
- Toys & Accessories
- Health & Grooming
- Training & Services
- Outdoor & Travel

### Key Messaging
- "Save on everything your dog loves"
- "Verified deals updated daily"
- "Your pup deserves the best for less"

## Conversion Optimization

### Trust Elements
- Deal verification badges
- User reviews/ratings
- Clear savings calculations
- Expiration date transparency

### Call-to-Actions
- "Copy Code" (primary action)
- "Get Deal" (secondary action)
- "View All [Store] Deals"

## Success Metrics
- Coupon copy rate
- Click-through to retailer
- User return visits
- Mobile vs desktop usage
- Category performance

This design brief ensures a user-friendly, trustworthy platform that makes finding and using pet deals effortless while maintaining a warm, dog-loving community feel.

1. Design Objective
Create a warm, energetic space where dog lovers instantly feel welcomed and confident they’re finding genuine savings for their furry friends. Everything from the layout to the smallest icon should reinforce trust, delight, and simplicity.
2. Visual Personality
Color Palette: Soft, cheerful hues—think warm yellows and gentle blues—that evoke sunshine and playfulness without overwhelming.
Typography:
Headings: A modern, friendly sans‑serif (like Inter) with open letterforms to feel approachable.
Body Copy: Highly legible sans‑serif with generous line spacing for comfort on small screens.
Accent Font: A slightly quirky, hand‑drawn style used sparingly for coupon codes and special call‑outs, giving a personal, “paw‑picked” touch.
Imagery & Icons: Real‑life photographs of happy dogs interspersed with clean line‑icons of bones, paw prints, and hearts. Rounded shapes and subtle shadows keep the look soft and contemporary.
3. Layout & Hierarchy
Hero Area:
Full‑bleed image of a joyful dog, overlaid with a single, punchy tagline (“Save on everything your dog loves”).
Prominent search bar centered to invite exploration.
Offer Grid:
Generous white space around each coupon card so the eye can rest and scan easily.
Coupon cards feature a bold discount label, brand logo, and a friendly “Get Deal” button.
A playful “Copied!” animation briefly replaces the button once the code is grabbed.
Navigation:
A fixed header with clear category labels (Food, Toys, Health, Services).
A secondary “Popular Stores” carousel below to spotlight key partners.
4. Interaction & Motion
Micro‑interactions:
Hover state for cards subtly lifts the card and deepens its shadow, inviting a click.
Copy‑code button pulses once on hover, hinting at its one‑click magic.
Transitions:
Smooth fades between deal filters and search results to reassure users that the site is responding.
Loading indicators shaped like spinning collars or wagging tails to keep the theme consistent.
5. Accessibility & Inclusivity
Ensure all text meets contrast standards so every pet parent—regardless of vision—can read offers with ease.
Interactive elements sized for easy tapping on touchscreens.
Alt‑text for all imagery describing dogs, products, and actions for screen‑reader users.
6. Emotional Tone
From the moment someone lands on TailTrove.com, they should feel the joy of treating their dog without guilt. Friendly copy (“Your pup deserves the best for less”) paired with bright visuals will create a sense of community and shared passion.
7. Success by Design
Scan‑ability: Users should spot great deals in under two seconds.
Trust Signals: Badges (“Verified Savings”), clear expiration dates, and reviewer star icons should feel earned and prominent.
Return Visits: A “My Favorite Deals” heart icon encourages saving and returning, reinforced by subtle reminders in the UI.
This design approach keeps dog lovers front and center—making sure every graphic, font choice, and interaction feels like it was lovingly tailored for them.

Target Market(s)

Dog Lovers looking for good deals

Industry/Entity Type

Coupon Code

Number of Pages Required

4 page

Font styles to use
Sans Serif

Requirements
Must have
• Modern look, coupon copy cards it's a deal site and I want the coupon code and copy in the coupon card, blog section, review section, modern footer/header
Nice to have
• Modern coupon code website, easy to use

```html
<!DOCTYPE html>
<html lang="en">
<head>
<meta charset="utf-8">
<title>Tail Trove – Dog Deals</title>
<link href="https://fonts.googleapis.com/css2?family=Inter:wght@400;500;600;700;800;900&family=Lato:wght@400;700;900&display=swap" rel="stylesheet">
<style>
:root{
  --blue:#2d7ad6;
  --blue-dark:#1f62b8;
  --yellow:#fcd63d;
  --yellow-soft:#f9dc5c;
  --ink:#1b1b1b;
  --muted:#555;
  --line:#d9d9d9;
  --green:#27b24a;
  --white:#fff;
  --black:#000;
  --grass:#4f8a2a;
}
*{box-sizing:border-box;margin:0;padding:0}
html,body{width:1200px;height:4736px;overflow:hidden;background:var(--white)}
body{position:relative;font-family:"Lato",sans-serif;color:var(--ink)}
.abs{position:absolute}
.h-title{font-family:"Inter",sans-serif;font-weight:500;font-size:42px;text-align:center;width:1200px;left:0}
.h-title span{color:var(--blue)}
.sub{font-size:21px;color:#444;text-align:center;width:1200px;left:0}
.btn{position:absolute;border-radius:30px;font-family:"Inter",sans-serif;font-weight:600;display:flex;align-items:center;justify-content:center}
.btn-blue{background:var(--blue);color:var(--white)}
.btn-yellow{background:var(--yellow);color:var(--ink)}

/* header */
.logo{display:flex;align-items:center;gap:12px;font-family:"Inter",sans-serif;font-weight:700;font-size:36px}
.logo i{width:44px;height:44px;border-radius:50%;background:var(--blue);display:block}
.nav{left:580px;top:26px;display:flex;gap:22px;font-family:"Inter",sans-serif;font-size:13px}
.nav .on{color:var(--blue);font-weight:600;border-bottom:3px solid var(--blue);padding-bottom:20px}

/* hero */
.hero{left:15px;top:75px;width:1170px;height:685px;border-radius:30px;background:linear-gradient(180deg,#5f9a33,#3e7a22);overflow:hidden}
.hero-dog{position:absolute;left:70px;top:20px;width:380px;height:460px;border-radius:40%;background:radial-gradient(circle,#e9e2d8,#b79a7a 60%,transparent 72%)}
.hero h1{position:absolute;left:535px;top:128px;font-family:"Inter",sans-serif;font-weight:900;font-size:60px;line-height:70px;color:var(--white)}
.search{position:absolute;left:130px;top:460px;width:910px;height:115px;border-radius:60px;background:rgba(240,245,230,.82);display:flex;align-items:center;gap:16px;padding-left:90px}
.sel{height:40px;border:2px solid var(--blue);border-radius:20px;background:var(--white);font-size:13px;display:flex;align-items:center;justify-content:space-between;padding:0 16px}
.dots{position:absolute;left:565px;top:625px;display:flex;gap:5px}
.dots b{width:9px;height:9px;border-radius:50%;background:var(--white)}
.dots b.a{background:var(--blue)}

/* categories */
.cat{top:935px;width:238px;height:260px;border-radius:12px;background:var(--white);box-shadow:0 0 0 3px #ececec,0 4px 12px rgba(0,0,0,.1);text-align:center;font-family:"Inter",sans-serif;font-size:23px;line-height:34px;padding-top:150px}
.cat::before{content:"";position:absolute;left:77px;top:42px;width:84px;height:84px;border-radius:50%;background:var(--blue)}
.cat.on{background:var(--yellow);box-shadow:0 0 0 3px var(--blue)}
.cat.on::before{box-shadow:0 0 0 4px var(--white)}
.arrow{width:28px;height:28px;border-radius:50%;display:flex;align-items:center;justify-content:center}

/* stores */
.stores{left:112px;top:1290px;width:976px;height:370px;border-radius:16px;background:linear-gradient(135deg,#3685d9,#2466b8)}
.store{top:152px;width:197px;height:73px;background:var(--white);border-radius:4px;display:flex;align-items:center;justify-content:center;gap:8px;font-family:"Inter",sans-serif;font-weight:600;font-size:22px;color:#333}
.store i{width:22px;height:22px;border-radius:50%;background:#c9c9c9;display:block}

/* coupons */
.coupon{top:1875px;width:236px;height:345px;border:3px dashed #e2e2e2;border-radius:12px;background:var(--white);padding:26px 18px}
.coupon.tilt{transform:rotate(4deg);border:3px solid var(--blue);box-shadow:0 6px 16px rgba(0,0,0,.12)}
.brand{display:inline-flex;align-items:center;gap:6px;border:1px solid #ccc;border-radius:4px;padding:8px 14px;font-family:"Inter",sans-serif;font-weight:700;font-size:14px;color:var(--blue)}
.brand i{width:12px;height:12px;background:var(--yellow);display:block}
.coupon h3{font-family:"Inter",sans-serif;font-weight:400;font-size:23px;margin-top:18px}
.coupon h3 b{color:var(--blue);font-weight:500}
.coupon p{font-size:14px;line-height:25px;margin-top:12px;color:#333}
.verified{position:absolute;left:18px;top:230px;display:flex;align-items:center;gap:8px;color:var(--green);font-size:14px}
.verified i{width:22px;height:22px;border-radius:50%;background:var(--green);display:flex;align-items:center;justify-content:center}
.coupon .btn{left:18px;top:275px;width:148px;height:36px;font-size:14px}

/* about */
.about-l{left:112px;top:2358px;width:490px;height:384px;background:var(--yellow-soft)}
.about-r{left:590px;top:2358px;width:498px;height:384px;background:linear-gradient(135deg,#d9d2c8,#8a6f58 60%,#3d3a38);border-radius:90px 0 0 0}

/* deals */
.prod{top:2955px;width:228px;height:320px;background:#ededed;border-radius:6px}
.prod.on{background:var(--white);border:3px solid var(--blue)}
.prod .tag{position:absolute;left:22px;top:20px;background:var(--yellow);border-radius:12px;padding:4px 12px;font-size:13px;font-weight:700}
.prod .ph{position:absolute;left:40px;top:70px;width:148px;height:170px;border-radius:10px}
.pinfo{top:3308px;font-family:"Inter",sans-serif}
.pinfo .c{font-size:14px}
.pinfo .s{color:#f06a1a;font-size:13px;letter-spacing:1px;margin-top:4px}
.pinfo .p{font-weight:700;font-size:16px;margin-top:6px}
.pinfo .p s{font-weight:400;color:#777;font-size:11px;margin-left:14px}

/* testimonials */
.testi{left:112px;top:3532px;width:978px;height:493px;border-radius:16px;background:linear-gradient(135deg,#3b88da,#2466b8);color:var(--white)}
.avatar{width:86px;height:86px;border-radius:50%;background:#8a7566;border:4px solid var(--white)}
.tname{font-family:"Inter",sans-serif;font-size:20px;font-weight:500}
.tstars{color:var(--yellow);font-size:22px;letter-spacing:2px}
.ttext{font-size:14px;line-height:28px}

/* footer */
.footer{left:15px;top:4305px;width:1170px;height:431px;background:var(--black);border-radius:30px 30px 0 0;color:var(--white)}
.fcol h4{font-family:"Inter",sans-serif;font-weight:600;font-size:21px;color:var(--blue);margin-bottom:16px}
.fcol li{list-style:none;font-size:14px;line-height:33px}
.social{display:flex;gap:8px}
.social i{width:26px;height:26px;border-radius:50%;background:var(--white);display:block}
</style>
</head>
<body>

<!-- Header -->
<header>
  <div class="abs logo" style="left:110px;top:14px"><i></i>Tail Trove</div>
  <nav class="abs nav">
    <span class="on">Home</span><span>Categories</span><span>Popular Stores</span><span>Latest Deals</span>
  </nav>
  <div class="btn btn-yellow" style="left:982px;top:18px;width:106px;height:34px;font-size:13px">Contact</div>
</header>

<!-- Hero -->
<section class="abs hero">
  <div class="hero-dog" role="img" aria-label="Photo of a happy terrier running on grass carrying a bone toy"></div>
  <h1>Save on everything<br>your dog loves</h1>
  <div class="btn btn-blue" style="left:544px;top:303px;width:120px;height:34px;font-size:13px;box-shadow:0 0 0 2px var(--white)">Get Started</div>
  <div class="search">
    <div class="sel" style="width:186px">By Category <span>⌄</span></div>
    <div class="sel" style="width:170px">Store <span>⌄</span></div>
    <div class="sel" style="width:228px">Discount Amount <span>⌄</span></div>
    <div class="btn btn-blue" style="position:static;width:120px;height:40px;font-size:13px">Search</div>
  </div>
  <div class="dots"><b></b><b class="a"></b><b></b></div>
</section>

<!-- Categories -->
<h2 class="abs h-title" style="top:838px">Deal <span>Categories</span></h2>
<div class="abs arrow" style="left:24px;top:1048px;background:var(--blue)"><svg width="14" height="14" viewBox="0 0 14 14"><path d="M12 7H3M7 3L3 7l4 4" stroke="#fff" stroke-width="2" fill="none"/></svg></div>
<div class="abs arrow" style="left:1131px;top:1048px;background:#bbb"><svg width="14" height="14" viewBox="0 0 14 14"><path d="M2 7h9M7 3l4 4-4 4" stroke="#fff" stroke-width="2" fill="none"/></svg></div>
<div class="abs cat" style="left:110px">Dog Food &amp;<br>Treats</div>
<div class="abs cat" style="left:356px">Toys &amp;<br>Accessories</div>
<div class="abs cat on" style="left:604px">Health &amp;<br>Grooming</div>
<div class="abs cat" style="left:850px">Training &amp;<br>Services</div>

<!-- Popular stores -->
<section class="abs stores">
  <h2 class="abs" style="left:72px;top:48px;font-family:Inter,sans-serif;font-weight:500;font-size:42px;color:#fff">Popular Stores</h2>
  <div class="abs arrow" style="left:870px;top:56px;background:#fff"><svg width="14" height="14" viewBox="0 0 14 14"><path d="M12 7H3M7 3L3 7l4 4" stroke="#2466b8" stroke-width="2" fill="none"/></svg></div>
  <div class="abs arrow" style="left:904px;top:56px;background:rgba(255,255,255,.35)"></div>
  <div class="abs store" style="left:63px"><i></i>Woofline</div>
  <div class="abs store" style="left:283px"><i></i>Snoutly</div>
  <div class="abs store" style="left:504px"><i></i>Pawtopia</div>
  <div class="abs store" style="left:724px"><i></i>Kennelry</div>
  <div class="btn btn-yellow" style="left:414px;top:275px;width:148px;height:36px;font-size:13px">View All Stores</div>
</section>

<!-- Coupons -->
<h2 class="abs h-title" style="top:1733px">Our <span>Coupon Cards</span></h2>
<p class="abs sub" style="top:1795px">Verified deals updated daily</p>

<div class="abs coupon" style="left:92px">
  <span class="brand" style="color:#333"><i></i>Parcelo</span>
  <h3>Up To <b>30%</b> Off</h3>
  <p>Get Up To 30% off<br>on Pet Food Combo</p>
  <div class="verified"><i><svg width="12" height="12" viewBox="0 0 12 12"><path d="M2 6l3 3 5-6" stroke="#fff" stroke-width="2" fill="none"/></svg></i>Verified</div>
  <div class="btn btn-blue">Get Deal</div>
</div>
<div class="abs coupon" style="left:348px">
  <span class="brand"><i></i>Cartnest</span>
  <h3>Up To <b>40%</b> Off</h3>
  <p>Get Up To 40% off<br>on Pet Food Combo</p>
  <div class="verified"><i><svg width="12" height="12" viewBox="0 0 12 12"><path d="M2 6l3 3 5-6" stroke="#fff" stroke-width="2" fill="none"/></svg></i>Verified</div>
  <div class="btn btn-blue">Get Deal</div>
</div>
<div class="abs coupon tilt" style="left:602px">
  <span class="brand" style="color:#111"><i></i>Voltmart</span>
  <h3>Up To <b>43%</b> Off</h3>
  <p>Get Up To 30% off<br>on Pet Food Combo</p>
  <div class="verified"><i><svg width="12" height="12" viewBox="0 0 12 12"><path d="M2 6l3 3 5-6" stroke="#fff" stroke-width="2" fill="none"/></svg></i>Verified</div>
  <div class="btn btn-yellow" style="border:2px solid var(--blue)">Copied Code</div>
</div>
<div class="abs coupon" style="left:866px">
  <span class="brand"><i></i>Shelfway</span>
  <h3>Up To <b>30%</b> Off</h3>
  <p>Get Up To 30% off<br>on Pet Food Combo</p>
  <div class="verified"><i><svg width="12" height="12" viewBox="0 0 12 12"><path d="M2 6l3 3 5-6" stroke="#fff" stroke-width="2" fill="none"/></svg></i>Verified</div>
  <div class="btn btn-blue">Get Deal</div>
</div>

<!-- About -->
<section class="abs about-l">
  <h2 class="abs" style="left:34px;top:42px;font-family:Inter,sans-serif;font-weight:800;font-size:40px">About Us</h2>
  <p class="abs" style="left:34px;top:108px;width:390px;font-size:14px;line-height:34px">Lorem ipsum dolor sit amet, consectetur adipiscing elit, sed do eiusmod tempor incididunt ut labore et dolore magna aliqua. Ut enim ad minim veniam, quis nostrud exercitation ullamco laboris nisi ut aliquip ex ea commodo consequat.</p>
  <div class="btn btn-blue" style="left:34px;top:292px;width:106px;height:34px;font-size:13px">Read More</div>
</section>
<div class="abs about-r" role="img" aria-label="Photo of a couple on a couch shopping online with their dog beside them"></div>

<!-- Latest deals -->
<h2 class="abs h-title" style="top:2833px">Latest <span>Deals</span></h2>
<p class="abs sub" style="top:2893px">Your pup deserves the best for less</p>

<div class="abs prod" style="left:107px"><span class="tag">-20 %</span><div class="ph" role="img" aria-label="Bag of dry dog food" style="background:linear-gradient(#d9b98a,#a9743f)"></div></div>
<div class="abs prod" style="left:357px"><span class="tag">-20 %</span><div class="ph" role="img" aria-label="Assorted colourful dog toys" style="background:linear-gradient(135deg,#f5d33a,#3c8ad8,#e24b4b)"></div></div>
<div class="abs prod on" style="left:604px"><span class="tag">-50 %</span>
  <div class="ph" role="img" aria-label="Dog wrapped in a towel with grooming tools" style="background:linear-gradient(135deg,#c9a26a,#2d5fb0);left:30px"></div>
  <div class="abs" style="left:190px;top:14px;width:22px;height:22px;border-radius:50%;background:#fff;box-shadow:0 1px 4px rgba(0,0,0,.2);color:#d62b3b;font-size:14px;text-align:center;line-height:22px">♥</div>
  <div class="abs" style="left:190px;top:44px;width:22px;height:22px;border-radius:50%;background:#fff;box-shadow:0 1px 4px rgba(0,0,0,.2)"></div>
  <div class="abs" style="left:190px;top:74px;width:22px;height:22px;border-radius:50%;background:#fff;box-shadow:0 1px 4px rgba(0,0,0,.2)"></div>
  <div class="btn btn-blue" style="left:56px;top:300px;width:112px;height:32px;font-size:13px">Shop Now</div>
</div>
<div class="abs prod" style="left:858px"><span class="tag">-20 %</span><div class="ph" role="img" aria-label="Dog leashes in several colours" style="background:linear-gradient(90deg,#8cc63e,#2d7ad6,#e24b2b,#7a3a2a)"></div></div>

<div class="abs pinfo" style="left:103px"><div class="c">DOG FOOD</div><div class="s">★★★★★</div><div class="p">$34.00<s>$40.00</s></div></div>
<div class="abs pinfo" style="left:353px"><div class="c">TOYS</div><div class="s">★★★★★</div><div class="p">$54.00<s>$65.00</s></div></div>
<div class="abs pinfo" style="left:600px"><div class="c">DOG GROOMING</div><div class="s">★★★★★</div><div class="p">$43.00<s>$50.00</s></div></div>
<div class="abs pinfo" style="left:854px"><div class="c">DOG ACCESSORIES</div><div class="s">★★★★★</div><div class="p">$3700<s>$47.00</s></div></div>
<div class="btn btn-blue" style="left:535px;top:3413px;width:130px;height:36px;font-size:13px">View All Deals</div>

<!-- Testimonials -->
<section class="abs testi">
  <h2 class="abs" style="left:0;width:978px;text-align:center;top:70px;font-family:Inter,sans-serif;font-weight:600;font-size:42px">Client Testimonials</h2>
  <div class="abs" style="left:489px;top:160px;height:240px;border-left:2px dashed #fff"></div>
  <div class="abs avatar" style="left:40px;top:180px" role="img" aria-label="Portrait of a reviewer"></div>
  <div class="abs tname" style="left:148px;top:192px">Maren Holt</div>
  <div class="abs tstars" style="left:148px;top:222px">● ★★★★★</div>
  <p class="abs ttext" style="left:42px;top:300px;width:410px">Sed ut perspiciatis unde omnis iste natus error sit voluptatem accusantium doloremque laudantium, totam rem aperiam, eaque ipsa quae ab illo inventore veritatis et quasi architecto beatae vitae dicta sunt explicabo.</p>
  <div class="abs avatar" style="left:538px;top:160px" role="img" aria-label="Portrait of a reviewer"></div>
  <div class="abs tname" style="left:645px;top:168px">Tobias &amp; Leena Varga</div>
  <div class="abs tstars" style="left:645px;top:198px">● ★★★★★</div>
  <p class="abs ttext" style="left:540px;top:268px;width:400px">Ut enim ad minima veniam, quis nostrum exercitationem ullam corporis suscipit laboriosam, nisi ut aliquid ex ea commodi. Quis autem vel eum iure reprehenderit qui in ea voluptate velit esse quam nihil molestiae.</p>
  <div class="abs" style="left:471px;top:448px;display:flex;gap:4px"><i style="width:9px;height:9px;border-radius:50%;background:#fff"></i><i style="width:9px;height:9px;border-radius:50%;background:#fff"></i><i style="width:9px;height:9px;border-radius:50%;background:#fff"></i></div>
</section>

<!-- Trust -->
<h2 class="abs" style="left:115px;top:4150px;font-family:Inter,sans-serif;font-weight:500;font-size:42px">Our <span style="color:var(--blue)">Trust</span></h2>
<div class="abs" style="left:566px;top:4118px;width:126px;height:126px;border-radius:50%;background:#8a8a8a"></div>
<div class="abs" style="left:740px;top:4100px;width:145px;height:145px;border-radius:50%;background:#fff;box-shadow:0 4px 14px rgba(0,0,0,.18)"><div style="margin:18px;width:109px;height:109px;border-radius:50%;background:#d9a21e"></div></div>
<div class="abs" style="left:954px;top:4118px;width:122px;height:122px;border-radius:50%;background:#a8a8a8"></div>

<!-- Footer -->
<footer class="abs footer">
  <div class="abs logo" style="left:95px;top:82px;color:#fff"><i style="background:#fff"></i>Tail Trove</div>
  <div class="abs" style="left:95px;top:173px;width:328px;height:48px;border-radius:24px;background:#fff;color:#666;font-size:12px;display:flex;align-items:center;padding-left:22px">Enter Email Address</div>
  <div class="btn btn-yellow" style="left:95px;top:235px;width:112px;height:32px;font-size:12px">Subscribe</div>
  <div class="abs social" style="left:95px;top:300px"><i></i><i></i><i></i><i></i></div>
  <div class="abs fcol" style="left:481px;top:80px"><h4>Quick Links</h4><ul><li>Home</li><li>About Us</li><li>Services</li><li>Insights</li><li>Services</li><li>Contact Us</li></ul></div>
  <div class="abs fcol" style="left:635px;top:80px"><h4>Other Links</h4><ul><li>Privacy Policy</li><li>Terms &amp; Conditions</li><li>Disclaimer</li><li>FAQ's</li><li>Support</li><li>Help</li></ul></div>
  <div class="abs fcol" style="left:837px;top:80px"><h4>Contact Info</h4>
    <ul>
      <li style="display:flex;gap:12px;align-items:center"><svg width="18" height="20" viewBox="0 0 18 20"><path d="M9 1a7 7 0 0 0-7 7c0 5 7 11 7 11s7-6 7-11a7 7 0 0 0-7-7z" fill="#2d7ad6"/><circle cx="9" cy="8" r="2.5" fill="#000"/></svg>Lorem Ipsum,USA -437916</li>
      <li style="display:flex;gap:12px;align-items:center;margin-top:30px"><svg width="20" height="20" viewBox="0 0 20 20"><circle cx="10" cy="10" r="10" fill="#2d7ad6"/><path d="M6 5l2 0 1 3-1.5 1a7 7 0 0 0 3.5 3.5l1-1.5 3 1v2a1 1 0 0 1-1 1A10 10 0 0 1 5 6a1 1 0 0 1 1-1z" fill="#fff"/></svg>888 888 8888</li>
      <li style="display:flex;gap:12px;align-items:center;margin-top:10px"><svg width="20" height="20" viewBox="0 0 20 20"><circle cx="10" cy="10" r="10" fill="#2d7ad6"/><rect x="5" y="6.5" width="10" height="7" fill="#fff"/><path d="M5 6.5l5 4 5-4" stroke="#2d7ad6" fill="none"/></svg>info@tailtrove.com</li>
    </ul>
  </div>
  <div class="abs" style="left:95px;top:345px;width:980px;border-top:1px solid #444"></div>
  <div class="abs" style="left:0;width:1170px;top:375px;text-align:center;font-size:13px">© 2025 Tail Trove .All rights reserved</div>
</footer>

</body>
</html>
```